50 Lessons from my entrepreneurial journey

make a book cover (see attached file for reference or sample )
https://files.example-share.net/file/d/7kPqWz3rTn8LmYv2XcB5dHj9QsF0aUe4G/view?usp=share_link

make a back book cover (see writings below)

BUILD A BUSINESS. BUILD A LIFE.

What does it really take to succeed, not just in business, but in life?

In MARLO’S LEDGER, award-winning entrepreneur, speaker, and columnist Marlo Dantes shares 50 powerful lessons and more drawn from over three decades of building Cebu’s most beloved homegrown brands. Honest, practical, and deeply personal, this book brings together timeless insights on entrepreneurship, leadership, family, faith, and the inner journey of growth.

Whether you’re just starting out, scaling up, or searching for clarity in the next chapter of your life, these pages will guide, inspire, and challenge you to pursue something greater not just profit, but purpose. More than a business book, this is a book about building the kind of life you won’t need a vacation from.

About the Author

Marlo Dantes is one of Cebu’s most respected and successful entrepreneurs, best known for building iconic homegrown brands such as Breezy Coolers and Blends, Hall of Roastmeat, and The PEAK of Cebu. As Chairman and CEO of the Dantes Food Group, he has spent over 25 years shaping the business landscape of the Visayas and Mindanao. Named Entrepreneur of the Year by the Cebu Guild of Traders and Makers and recognized for one of the Top Ten Most Outstanding Family Businesses in the Philippines, Marlo is also a popular columnist for DayLamp Cebu. Through his writing and mentorship, he continues to empower the next generation to build with heart, lead with purpose, and live with meaning.

Target Market(s)

Millennials & Young Professionals

Industry/Entity Type

Entrepreneurship

Font styles to use
Serif
Sans Serif

Requirements
Must have
• Professional yet clean modern typography

```html
<!DOCTYPE html>
<html lang="en">
<head>
<meta charset="utf-8">
<title>Marlo’s Ledger – Book Cover Spread</title>
<link rel="stylesheet" href="https://fonts.googleapis.com/css2?family=Archivo+Black&family=Inter:wght@300;400;700&family=Libre+Baskerville&family=Oswald:wght@500;700&family=Yellowtail&display=block">
<style>
  :root {
    --backdrop: #b1b1b3;
    --charcoal: #2c2a2e;
    --paper: #ffffff;
    --gold: #e6a823;
    --gold-light: #f2d98a;
    --bronze: #b27a48;
    --yellow-text: #e9c23f;
    --body-grey: #c9c8cb;
    --ink: #1e1c1f;
    --tile-sky: #bcc8d6;
    --tile-dark: #0d0d0d;
  }
  * { margin: 0; padding: 0; box-sizing: border-box; }
  html, body { width: 1200px; height: 984px; overflow: hidden; background: var(--backdrop); }
  .canvas { position: relative; width: 1200px; height: 984px; }

  .back-cover { position: absolute; left: 130px; top: 126px; width: 439px; height: 699px; background: var(--charcoal); overflow: hidden; }
  .spine { position: absolute; left: 569px; top: 126px; width: 47px; height: 699px;
    background: linear-gradient(180deg, var(--gold) 0%, #e2ac45 45%, var(--bronze) 100%); overflow: hidden; }
  .front-cover { position: absolute; left: 616px; top: 126px; width: 439px; height: 699px; background: var(--paper); }

  /* back cover */
  .back-headline { position: absolute; left: 72px; top: 68px; color: #fff; line-height: 1; }
  .back-headline .line-light { font-family: "Inter", sans-serif; font-weight: 400; font-size: 25px; letter-spacing: -0.3px; display: block; }
  .back-headline .line-bold { font-family: "Archivo Black", sans-serif; font-size: 23px; display: block; margin-top: -2px; }
  .back-question { position: absolute; left: 72px; top: 129px; width: 310px; font-family: "Inter", sans-serif; font-weight: 700; font-size: 10px; line-height: 12.5px; color: var(--yellow-text); }
  .back-copy { position: absolute; left: 72px; top: 165px; width: 332px; font-family: "Inter", sans-serif; font-weight: 300; font-size: 10.1px; line-height: 13.1px; color: var(--body-grey); }
  .back-copy p { text-align: justify; margin-bottom: 13.1px; hyphens: auto; }
  .back-copy .about-heading { text-align: left; }
  .author-photo { position: absolute; left: 0; top: 503px; width: 212px; height: 196px;
    background: radial-gradient(ellipse at 45% 30%, #c79a80 0%, #8a6a5c 28%, #2a2a2e 62%, #1a1a1c 100%);
    border-radius: 90px 90px 0 0; }
  .author-name { position: absolute; left: 238px; top: 530px; line-height: 0.95;
    background: linear-gradient(90deg, var(--gold) 0%, var(--gold-light) 100%);
    -webkit-background-clip: text; background-clip: text; color: transparent; }
  .author-name .first { font-family: "Archivo Black", sans-serif; font-size: 34px; display: block; }
  .author-name .last { font-family: "Archivo Black", sans-serif; font-size: 34px; display: block; letter-spacing: 0.5px; }

  /* spine */
  .spine-art { position: absolute; left: 0; top: 0; }
  .spine-title, .spine-number { font-family: "Oswald", sans-serif; font-weight: 700; }
  .spine-subtitle { font-family: "Oswald", sans-serif; font-weight: 500; }

  /* front cover */
  .front-art { position: absolute; left: 0; top: 0; }
  .tagline { position: absolute; left: 0; width: 439px; top: 35px; text-align: center; font-family: "Inter", sans-serif; font-size: 9.5px; letter-spacing: 2.6px; color: #c99a1a; }
  .review-source { position: absolute; left: 0; width: 439px; top: 54px; text-align: center; font-family: "Inter", sans-serif; font-size: 9.5px; color: #c99a1a; }
  .title-script { font-family: "Yellowtail", cursive; }
  .title-main, .lessons-number, .lessons-label { font-family: "Oswald", sans-serif; }
  .seal-stars { font-family: "Inter", sans-serif; }
  .seal-label { font-family: "Libre Baskerville", serif; }
</style>
</head>
<body>
<main class="canvas">

  <section class="back-cover">
    <h2 class="back-headline">
      <span class="line-light">BUILD A BUSINESS.</span>
      <span class="line-bold">BUILD A LIFE.</span>
    </h2>
    <p class="back-question">WHAT DOES IT REALLY TAKE TO SUCCEED, NOT JUST IN BUSINESS, BUT IN LIFE?</p>
    <div class="back-copy">
      <p>In MARLO’S LEDGER, award-winning entrepreneur, speaker, and columnist Marlo Dantes shares 50 powerful lessons and more drawn from over three decades of building Cebu’s most beloved homegrown brands. Honest, practical, and deeply personal, this book brings together timeless insights on entrepreneurship, leadership, family, faith, and the inner journey of growth.</p>
      <p>Whether you’re just starting out, scaling up, or searching for clarity in the next chapter of your life, these pages will guide, inspire, and challenge you to pursue something greater not just profit, but purpose. More than a business book, this is a book about building the kind of life you won’t need a vacation from.</p>
      <p class="about-heading">About the Author</p>
      <p>Marlo Dantes is one of Cebu’s most respected and successful entrepreneurs, best known for building iconic homegrown brands such as Breezy Coolers and Blends, Hall of Roastmeat, and The PEAK of Cebu. As Chairman and CEO of the Dantes Food Group, he has spent over 25 years shaping the business landscape of the Visayas and Mindanao. Named Entrepreneur of the Year by the Cebu Guild of Traders and Makers and recognized for one of the Top Ten Most Outstanding Family Businesses in the Philippines, Marlo is also a popular columnist for DayLamp Cebu. Through his writing and mentorship, he continues to empower the next generation to build with heart, lead with purpose, and live with meaning.</p>
    </div>
    <div class="author-photo" role="img" aria-label="Portrait photo of the author in a dark suit and white shirt"></div>
    <div class="author-name">
      <span class="first">MARLO</span>
      <span class="last">DANTES</span>
    </div>
  </section>

  <section class="spine">
    <svg class="spine-art" width="47" height="699" viewBox="0 0 47 699" xmlns="http://www.w3.org/2000/svg">
      <text class="spine-title" transform="translate(10 48) rotate(90)" font-size="33" fill="#1e1c1f" textLength="177" lengthAdjust="spacingAndGlyphs">MARLO’S LEDGER</text>
      <rect class="spine-number-block" x="0" y="233" width="47" height="49" fill="#2c2a2e"/>
      <text class="spine-number" transform="translate(13 245) rotate(90)" font-size="27" fill="#e6a823" textLength="26" lengthAdjust="spacingAndGlyphs">50</text>
      <text class="spine-subtitle" transform="translate(15 287) rotate(90)" font-size="19" fill="#1e1c1f" textLength="321" lengthAdjust="spacingAndGlyphs">LESSONS FROM MY ENTREPRENEURIAL JOURNEY</text>
    </svg>
  </section>

  <section class="front-cover">
    <p class="tagline">INSIGHTFUL.PRACTICAL.INSPIRING.</p>
    <p class="review-source">- DAY LAMP -</p>
    <svg class="front-art" width="439" height="699" viewBox="616 126 439 699" xmlns="http://www.w3.org/2000/svg">
      <defs>
        <linearGradient id="title-gold" x1="0" x2="1" y1="0" y2="0">
          <stop offset="0" stop-color="#e6a823"/>
          <stop offset="0.5" stop-color="#f3dc95"/>
          <stop offset="1" stop-color="#b07a45"/>
        </linearGradient>
        <linearGradient id="seal-gold" x1="0" x2="1" y1="0" y2="1">
          <stop offset="0" stop-color="#f2c64a"/>
          <stop offset="1" stop-color="#dea22a"/>
        </linearGradient>
      </defs>

      <text class="title-script" x="700" y="283" font-size="58" fill="#1e1c1f" textLength="152" lengthAdjust="spacingAndGlyphs">Marlo’s</text>
      <text class="title-main" x="733" y="366" textLength="207" lengthAdjust="spacingAndGlyphs" font-weight="700" font-size="105" fill="url(#title-gold)">LEDGER</text>

      <g class="portrait-mosaic" role="img" aria-label="Author portrait split into a grid of square tiles">
        <g fill="#bcc8d6">
          <rect x="733" y="375" width="27" height="33"/><rect x="768" y="375" width="27" height="33"/><rect x="805" y="375" width="27" height="33"/><rect x="840" y="375" width="27" height="33"/><rect x="877" y="375" width="27" height="33"/><rect x="912" y="375" width="27" height="33"/>
          <rect x="733" y="418" width="27" height="33"/><rect x="768" y="418" width="27" height="33"/><rect x="805" y="418" width="27" height="33"/><rect x="840" y="418" width="27" height="33"/><rect x="877" y="418" width="27" height="33"/><rect x="912" y="418" width="27" height="33"/>
          <rect x="733" y="461" width="27" height="33"/><rect x="768" y="461" width="27" height="33"/><rect x="805" y="461" width="27" height="33"/><rect x="840" y="461" width="27" height="33"/><rect x="877" y="461" width="27" height="33"/><rect x="912" y="461" width="27" height="33"/>
          <rect x="733" y="504" width="27" height="33"/><rect x="768" y="504" width="27" height="33"/><rect x="805" y="504" width="27" height="33"/><rect x="840" y="504" width="27" height="33"/><rect x="877" y="504" width="27" height="33"/><rect x="912" y="504" width="27" height="33"/>
        </g>
        <g fill="#0d0d0d">
          <rect x="733" y="547" width="27" height="33"/><rect x="768" y="547" width="27" height="33"/><rect x="805" y="547" width="27" height="33"/><rect x="840" y="547" width="27" height="33"/><rect x="877" y="547" width="27" height="33"/><rect x="912" y="547" width="27" height="33"/>
          <rect x="733" y="590" width="27" height="33"/><rect x="768" y="590" width="27" height="33"/><rect x="805" y="590" width="27" height="33"/><rect x="840" y="590" width="27" height="33"/><rect x="877" y="590" width="27" height="33"/><rect x="912" y="590" width="27" height="33"/>
          <rect x="733" y="634" width="27" height="33"/><rect x="768" y="634" width="27" height="33"/><rect x="805" y="634" width="27" height="33"/><rect x="840" y="634" width="27" height="33"/><rect x="877" y="634" width="27" height="33"/><rect x="912" y="634" width="27" height="33"/>
          <rect x="733" y="677" width="27" height="33"/><rect x="768" y="677" width="27" height="33"/><rect x="805" y="677" width="27" height="33"/><rect x="840" y="677" width="27" height="33"/><rect x="877" y="677" width="27" height="33"/><rect x="912" y="677" width="27" height="33"/>
          <rect x="733" y="720" width="27" height="33"/><rect x="768" y="720" width="27" height="33"/>
        </g>
      </g>

      <text class="lessons-number" x="805" y="754" font-weight="700" font-size="40" fill="#c9a21c" textLength="35" lengthAdjust="spacingAndGlyphs">50</text>
      <g class="lessons-label" font-weight="500" font-size="12.5" fill="#1e1c1f">
        <text x="846" y="731" textLength="78" lengthAdjust="spacingAndGlyphs">LESSONS FROM MY</text>
        <text x="846" y="742.5" textLength="78" lengthAdjust="spacingAndGlyphs">ENTREPRENEURIAL</text>
        <text x="846" y="754">JOURNEY</text>
      </g>

      <g class="award-seal" transform="translate(948 479)">
        <polygon fill="url(#seal-gold)" points="48,0 39.6,10.6 41.6,24 29,29 24,41.6 10.6,39.6 0,48 -10.6,39.6 -24,41.6 -29,29 -41.6,24 -39.6,10.6 -48,0 -39.6,-10.6 -41.6,-24 -29,-29 -24,-41.6 -10.6,-39.6 0,-48 10.6,-39.6 24,-41.6 29,-29 41.6,-24 39.6,-10.6"/>
        <text class="seal-stars" x="0" y="-14" text-anchor="middle" font-size="8" fill="#fff">★ ★ ★</text>
        <g class="seal-label" font-size="6.6" fill="#fff" text-anchor="middle">
          <text x="0" y="-1">AWARD</text>
          <text x="0" y="6">WINNING</text>
          <text x="0" y="13">ENTREPRENEUR</text>
        </g>
      </g>
    </svg>
  </section>

</main>
</body>
</html>
```